Website and Mobile Devices design for food related application.

We need a design that is simple yet playful. The design should be food related if possible.
This design will be on the website and the mobile platform markets we intend application to be deployed too.
This application/website is called "Pickvoro[.com]. Its a random restaurant picker for the indecisive users.
Updates
Hi all, I picked a design. Again lots of great designs were submitted but I picked one that was more in line with what I wanted.
Target Market(s)
young internet savvy users.
Industry/Entity Type
Restaurant
Look and feel
Each slider illustrates characteristics of the customer's brand and the style your logo design should communicate.

```html
<!DOCTYPE html>
<html lang="en">
<head>
<meta charset="utf-8">
<title>Pickvoro – random restaurant picker</title>
<link href="https://fonts.googleapis.com/css2?family=Lilita+One&family=Arimo:wght@400&display=swap" rel="stylesheet">
<style>
  :root{
    --header-bg:#bb5a2f;
    --hero-top:#f0904a;
    --hero-bottom:#e2773a;
    --brown-dark:#6e3515;
    --panel-warm:#a0522d;
    --panel-deep:#7a3a1a;
    --accent:#fdb813;
    --text:#6b5a55;
    --white:#ffffff;
    --rule:#8a4a2a;
  }
  *{box-sizing:border-box;margin:0;padding:0}
  html,body{width:1200px;height:1000px;overflow:hidden;background:var(--white)}
  body{font-family:"Arimo",Arial,sans-serif;color:var(--text);position:relative}
  .display{font-family:"Lilita One",sans-serif;font-weight:400}

  .site-header{position:absolute;top:0;left:0;width:1200px;height:82px;background:var(--header-bg);z-index:2;
    border-bottom:2px dotted #d9844f}
  .brand{position:absolute;left:120px;top:18px;font-size:36px;color:var(--white);letter-spacing:.3px}
  .main-nav{position:absolute;right:120px;top:24px;display:flex;gap:48px}
  .main-nav a{display:flex;align-items:center;gap:8px;color:var(--accent);text-decoration:none;font-size:21px}

  .hero{position:absolute;top:0;left:0;width:1200px;height:557px;
    background:linear-gradient(180deg,var(--hero-top),var(--hero-bottom))}
  .hero-visual{position:absolute;left:390px;top:95px;width:700px;height:462px;
    background:radial-gradient(ellipse at 55% 60%,#f3a468 0%,rgba(240,144,74,0) 70%)}
  .hero-title{position:absolute;left:120px;top:186px;font-size:68px;line-height:72px;color:var(--brown-dark);
    font-style:italic}
  .hero-sub{position:absolute;left:120px;top:346px;font-size:46px;line-height:50px;color:var(--white)}

  .intro{position:absolute;left:120px;top:596px;width:960px;text-align:center;font-size:16px;line-height:26px}

  .panel{position:absolute;top:703px;width:460px;height:292px;border-bottom:2px solid var(--rule)}
  .panel-any{left:120px}
  .panel-mood{left:620px}
  .panel-head{height:60px;display:flex;align-items:center;justify-content:center;color:var(--white);font-size:30px}
  .panel-any .panel-head{background:var(--panel-warm)}
  .panel-mood .panel-head{background:var(--panel-deep)}
  .panel-text{margin-top:24px;font-size:16px;line-height:26px}
  .cuisines{margin-top:26px;display:grid;grid-template-columns:150px 150px 150px;row-gap:20px}
  .cuisines label{display:flex;align-items:center;gap:8px;font-size:16px;height:20px}
  .cuisines input{appearance:none;width:18px;height:18px;border:1.5px solid var(--text);border-radius:4px;background:var(--white)}
  .btn{position:absolute;left:100px;top:214px;width:250px;height:50px;border-radius:25px;background:var(--accent);
    color:var(--white);font-size:21px;display:flex;align-items:center;justify-content:center;text-decoration:none}
</style>
</head>
<body>
  <section class="hero">
    <div class="hero-visual" role="img" aria-label="Photo of a puzzled man in a white t-shirt with chalk thought bubbles of pizza and a taco"></div>
    <h1 class="hero-title display">Tough choice<br>huh?! ...</h1>
    <p class="hero-sub display">Well not<br>any more!</p>
  </section>

  <header class="site-header">
    <div class="brand display">Pickvoro</div>
    <nav class="main-nav display">
      <a href="#">
        <svg width="24" height="24" viewBox="0 0 24 24" fill="none" stroke="#fff" stroke-width="1.6" stroke-linejoin="round"><path d="M2 12 12 3l10 9"/><path d="M5 10v11h5v-6h4v6h5V10"/></svg>
        home</a>
      <a href="#">
        <svg width="24" height="24" viewBox="0 0 24 24" fill="none" stroke="#fff" stroke-width="1.6" stroke-linejoin="round"><path d="M3 4h18v12H11l-5 4v-4H3z"/></svg>
        contact us</a>
    </nav>
  </header>

  <p class="intro">Lorem ipsum dolor sit amet, consectetur adipisicing elit, sed do eiusmod tempor incididunt ut labore et dolore magna aliqua. Ut enim ad minim veniam, quis nostrud exercitation ullamco laboris nisi ut aliquip ex ea commodo consequat. Duis aute irure dolor in reprehenderit in voluptate velit esse cillum dolore eu fugiat nulla pariatur. Excepteur sint occaecat cupidatat non proident.</p>

  <section class="panel panel-any">
    <h2 class="panel-head display">I just wanna eat! ...</h2>
    <p class="panel-text">Lorem ipsum dolor sit amet, consectetur adipisicing elit, sed do eiusmod tempor incididunt ut labore et dolore magna aliqua. Ut enim ad minim veniam, quis nostrud exercitation ullamco laboris nisi ut aliquip ex ea commodo consequat.</p>
    <a class="btn display" href="#">find me anything!</a>
  </section>

  <section class="panel panel-mood">
    <h2 class="panel-head display">I’m in the mood for ...</h2>
    <form class="cuisines">
      <label><input type="checkbox">Mexican</label>
      <label><input type="checkbox">Italian</label>
      <label><input type="checkbox">Greek</label>
      <label><input type="checkbox">Portuguese</label>
      <label><input type="checkbox">Pizza</label>
      <label><input type="checkbox">Burger</label>
      <label><input type="checkbox">BBQ</label>
      <label><input type="checkbox">French</label>
      <label><input type="checkbox">Jamaican</label>
    </form>
    <a class="btn display" href="#">narrow it down!</a>
  </section>
</body>
</html>
```